Vetern Mailer for Mortgage Refinance

Hello, I need some options in my KT mailers we send out here in the USA! A sample of our mailer has been included. I need all the verbiage the same. The data merge points need to stay on too. Please make this pop. We have a high end DELMO printer and a Z auto folding machine. Letter goes into a number 10 envelope with windows. So lets see what you can do. One with colors below is our company colors and then one black, white, gray.
Blue - 3399FF------ R 51 G 153 B 255
Orange - FF9933----- R 255 G 153 B 51
Black – 333333------ R 51 G 51 B 51
White – FFFFFF------ R 255 G 255 B 255

Target Market(s)

United States Military Service Members

Industry/Entity Type

Mortgage Lender

Requirements
Must have
• Margins for folding with Z and Number 10 Envelope with two windows

```html
<!DOCTYPE html>
<html lang="en">
<head>
<meta charset="utf-8">
<title>KT Loan Mailer – Ridgeline Home Loans</title>
<link href="https://fonts.googleapis.com/css2?family=Arimo:wght@400;700&display=swap" rel="stylesheet">
<style>
  :root {
    --backdrop: #b3b0b1;
    --paper: #ffffff;
    --brand-blue: #4a89c8;
    --brand-orange: #f79a3a;
    --ink: #111111;
  }
  * { box-sizing: border-box; margin: 0; padding: 0; }
  html, body { width: 1200px; height: 1200px; overflow: hidden; }
  body {
    background: var(--backdrop);
    font-family: "Arimo", Arial, sans-serif;
    color: var(--ink);
    position: relative;
  }
  .letter {
    position: absolute;
    left: 229px; top: 75px;
    width: 743px; height: 1050px;
    background: var(--paper);
    font-size: 13.6px;
    line-height: 18.5px;
  }
  .letter-frame { position: absolute; inset: 0; width: 100%; height: 100%; }
  .block { position: absolute; }
  .center { text-align: center; }
  b { font-weight: 700; }
  sup { font-size: 0.6em; line-height: 0; vertical-align: 0.6em; }

  .reference { left: 51px; top: 57px; }
  .skip-offer { left: 510px; top: 57px; width: 176px; }
  .skip-offer .amount { font-size: 28px; font-weight: 700; line-height: 34px; margin-top: 6px; }
  .affiliation { left: 51px; top: 146px; font-size: 10px; line-height: 13px; }
  .recipient { left: 73px; top: 220px; }
  .defer-note { left: 700px; top: 222px; transform: translateX(-100%); text-align: center; width: 220px; left: 484px; }
  .call-box { left: 484px; top: 290px; width: 220px; }
  .call-box .phone { font-size: 15px; font-weight: 700; }
  .salutation { left: 51px; top: 350px; }
  .intro { left: 51px; top: 400px; width: 610px; }
  .escrow-note { left: 0; right: 0; top: 535px; }

  .benefits { top: 573px; }
  .benefits h2 {
    font-size: 15px; font-weight: 700; text-decoration: underline;
    line-height: 20px;
  }
  .benefits ul { list-style: none; }
  .benefits li::before { content: "• "; }
  .benefits-general { left: 51px; }
  .benefits-irrrl { left: 419px; }

  .call-to-action { left: 0; right: 0; top: 708px; }
  .wordmark {
    left: 0; right: 0; top: 790px;
    font-size: 58px; line-height: 70px;
    font-weight: 400; letter-spacing: 6px;
    color: var(--brand-blue);
  }
  .contact-footer { left: 0; right: 0; top: 886px; }
  .cash-out {
    left: 238px; top: 932px; width: 266px; height: 27px;
    background: var(--brand-orange); color: #fff;
    font-size: 11.5px; font-weight: 700; line-height: 27px;
  }
  .company-line { left: 0; right: 0; top: 967px; font-size: 11px; line-height: 14px; }
  .company-line small { display: block; font-size: 8px; line-height: 10px; }
</style>
</head>
<body>
  <main class="letter">
    <svg class="letter-frame" viewBox="0 0 594 840" preserveAspectRatio="none" aria-hidden="true">
      <rect x="0" y="0" width="594" height="30" fill="var(--brand-orange)"/>
      <polygon points="296,30 365,30 365,108 300,38" fill="var(--brand-orange)"/>
      <polyline points="0,40 291,40 371,122 371,40 594,40" fill="none" stroke="var(--brand-blue)" stroke-width="2"/>
      <rect x="90" y="813" width="187" height="14" fill="var(--brand-blue)"/>
      <rect x="277" y="813" width="227" height="14" fill="var(--brand-orange)"/>
    </svg>

    <div class="block reference">
      <p>RE: &lt;&lt;lender&gt;&gt;</p>
      <p>Loan ID Number: &lt;&lt;loan_id&gt;&gt;</p>
    </div>

    <div class="block skip-offer center">
      <p>&lt;&lt;close_month&gt;&gt; &amp; &lt;&lt;skip_<br>month&gt;&gt;</p>
      <p class="amount">$0</p>
    </div>

    <p class="block affiliation">Ridgeline Home Loans LLC Is not affiliated with your<br>current lender nor is it an agency of the Federal Government.</p>

    <address class="block recipient" style="font-style:normal">
      &lt;&lt;first_name&gt;&gt; &lt;&lt;last_name&gt;&gt;<br>
      &lt;&lt;address&gt;&gt;<br>
      &lt;&lt;city_state_zip&gt;&gt;
    </address>

    <p class="block defer-note">You may be able to defer<br>your next two payments.<sup>1</sup></p>

    <div class="block call-box center">
      <p>Call toll-free</p>
      <p class="phone">&lt;&lt;phone_number&gt;&gt;</p>
      <p>Weekdays 6 a.m. to 5 p.m. PST</p>
    </div>

    <p class="block salutation">Dear &lt;&lt;first_name&gt;&gt;,</p>

    <p class="block intro">We are contacting you regarding your &lt;&lt;balance&gt;&gt; KT loan. Our review has indicated that because of homes appreciating in &lt;&lt;city&gt;&gt;, you may now qualify for additional benefits. These benefits may include lowering your monthly mortgage payment, deferring up to two payments, refund of escrow, and <b>$35,000</b> or more cash-out.3 Call our KT Program Specialist at <b>&lt;&lt;phone_number&gt;&gt;</b> at your earliest convenience to receive a detailed explanation of how you may be able to access these benefits.<sup>4</sup></p>

    <p class="block escrow-note center">You may also receive a check back from your escrow account.<sup>2</sup></p>

    <section class="block benefits benefits-general">
      <h2>Additional Benefits Include:</h2>
      <ul>
        <li>100% LTV Cash-Out Available</li>
        <li>Pay off High Interest Debt</li>
        <li>Complete a long overdue home renovation</li>
        <li>No out-of-pocket appraisal deposit</li>
        <li>No Private Mortgage Insurance</li>
      </ul>
    </section>

    <section class="block benefits benefits-irrrl">
      <h2>KT IRRRL Benefits:</h2>
      <ul>
        <li>Reduce Your Current Interest Rate</li>
        <li>Mortgage-Only Credit Report</li>
        <li>No Appraisal Required</li>
        <li>Fast Closings in 8-14 days</li>
        <li>No Income or Asset Verification Required</li>
      </ul>
    </section>

    <p class="block call-to-action center">We recommend you call our office at <b>&lt;&lt;phone_number&gt;&gt;</b> within the next 3-5 business days<br>as market rates fluctuate. By taking action now your next mortgage payment may not be<br>due until &lt;&lt;next_pay_month&gt;&gt;.<sup>2</sup> To avoid further delay, please call today.</p>

    <p class="block wordmark center">RIDGELINE</p>

    <div class="block contact-footer center">
      <p>Phone : <b>&lt;&lt;phone_number&gt;&gt;</b></p>
      <p>Loan ID Number: &lt;&lt;loan_id&gt;&gt;</p>
    </div>

    <p class="block cash-out center">Cash Out Options (Tax Free): $35,000 or more</p>

    <p class="block company-line center">Ridgeline Home Loans LLC NMLS 4410982 2870 E Canyon View Dr Ste 120 Mesa, AZ 85213<small>*Please see reverse for disclaimer</small></p>
  </main>
</body>
</html>
```